Psychology and Counselling Relationship Centre wants a Website

We need a SEO Website that is professional and simple Company Logo and colours is done and supplied

Target Market(s)

People wanting marriage Counselling / Parenting Issues / Relationship issues

Industry/Entity Type

Psychology

Coding

Coded - Design and coding required

Number of Pages Required

5+ page

Font styles to use
Other font styles liked:
• calibri

Colors
32a6d6
33b8a4
0758a5

Requirements
Must have
• Simple easy layout
• Page by page link
• Easy to navigate
• Professional and Welcoming

```html
<!DOCTYPE html>
<html lang="en">
<head>
<meta charset="utf-8">
<title>Whole Heart Wellbeing — Psychology &amp; Counselling</title>
<link href="https://fonts.googleapis.com/css2?family=Open+Sans:wght@300;400;600;700&family=Roboto:wght@300;400;500&display=swap" rel="stylesheet">
<style>
:root{
  --blue:#0758a5;
  --navy:#0e3f93;
  --nav:#2b63ad;
  --teal:#33b8a4;
  --sky:#32a6d6;
  --ink:#1d1d1d;
  --grey:#555;
  --line:#d6d6d6;
}
*{margin:0;padding:0;box-sizing:border-box}
html,body{width:1200px;height:3070px;overflow:hidden}
body{position:relative;background:#fff;font-family:"Roboto",sans-serif;color:var(--ink)}
.abs{position:absolute}

/* header */
.brand{left:100px;top:38px;display:flex;align-items:center;gap:14px}
.brand-mark{width:56px;height:56px;border-radius:50%;background:var(--teal)}
.brand-name{font-family:"Open Sans",sans-serif;font-weight:700;font-size:30px;color:var(--blue);line-height:1}
.brand-sub{font-family:"Open Sans",sans-serif;font-weight:700;font-size:14px;color:var(--blue);margin-top:6px;letter-spacing:.2px}
.contact-info{font-family:"Open Sans",sans-serif;font-weight:600;font-size:15px;color:#333;line-height:33px}
.ci-a{left:597px;top:38px}
.ci-b{left:826px;top:38px}

.mainnav{left:0;top:126px;width:1200px;height:67px;background:var(--nav);display:flex;align-items:center;padding-left:112px}
.mainnav a{font-family:"Open Sans",sans-serif;font-weight:600;font-size:16px;color:#fff;text-decoration:none;height:67px;line-height:67px;padding:0 6px}
.mainnav a.on{border-bottom:4px solid #fff}

/* hero */
.hero-photo{left:0;top:193px;width:1200px;height:600px;background:linear-gradient(100deg,#6f6a68 0%,#b9b3ab 30%,#e9e5de 55%,#5b7fa6 75%,#d8d9dc 100%)}
.hero-panel{left:128px;top:352px;width:406px;height:245px;border-radius:0 60px 0 60px;background:linear-gradient(135deg,rgba(51,184,164,.92),rgba(7,88,165,.92));text-align:center;padding-top:48px}
.hero-panel h1{font-family:"Open Sans",sans-serif;font-weight:600;font-size:34px;line-height:45px;color:#fff}
.ghost-btn{display:inline-block;margin-top:14px;border:2px solid #fff;border-radius:30px;width:174px;height:48px;line-height:44px;color:#fff;font-family:"Open Sans",sans-serif;font-weight:600;font-size:17px}
.dots{left:550px;top:691px;display:flex;gap:13px}
.dots i{width:10px;height:10px;border-radius:50%;background:#fff;display:block}
.dots i.on{background:transparent;border:2px solid #fff}
.wave{left:0;top:680px}

/* who we help */
.who-photo{left:140px;top:858px;width:400px;height:335px;border-radius:0 60px 0 60px;background:linear-gradient(135deg,#4f7fbf 0%,#7aa6cf 50%,#6fcfbd 100%)}
.who-title{left:585px;top:872px;font-family:"Open Sans",sans-serif;font-weight:700;font-size:36px;color:#111}
.who-text{left:588px;top:943px;width:530px;font-size:16px;line-height:30px;color:var(--grey)}
.pill{border-radius:30px;text-align:center;font-family:"Open Sans",sans-serif;font-weight:600}
.who-btn{left:588px;top:1113px;width:182px;height:56px;line-height:52px;border:2px solid var(--teal);color:var(--teal);font-size:18px;box-shadow:0 4px 10px rgba(0,0,0,.08)}

/* expect */
.expect{left:0;top:1277px;width:1200px;height:459px;background:linear-gradient(180deg,var(--teal) 0%,#2ea7b6 55%,var(--sky) 100%);text-align:center;color:#fff}
.expect h2{font-family:"Open Sans",sans-serif;font-weight:400;font-size:38px;margin-top:91px}
.expect p{font-size:18px;line-height:24px;width:850px;margin:22px auto 0}
.expect p+p{margin-top:24px}
.expect .pill{display:inline-block;margin-top:30px;width:180px;height:54px;line-height:54px;background:#fff;color:var(--teal);font-size:18px}

/* services */
.services{left:0;top:1736px;width:1200px;height:496px;background:linear-gradient(180deg,#e4e8ef,#f2f3f6)}
.card{top:1838px;width:225px;height:310px;background:#fff;border-radius:0 50px 0 50px;text-align:center;padding:0 18px;box-shadow:0 4px 14px rgba(0,0,0,.06)}
.card-icon{position:absolute;left:62px;top:-47px;width:100px;height:100px;border-radius:50%;background:#fff;padding:6px}
.card-icon span{display:block;width:88px;height:88px;border-radius:50%;background:radial-gradient(circle at 50% 40%,#2a6fc4,var(--navy))}
.card h3{font-family:"Open Sans",sans-serif;font-weight:600;font-size:18px;margin-top:66px;color:#222;line-height:23px}
.card p{font-size:12px;line-height:18.5px;color:#555;margin-top:8px}
.card .pill{position:absolute;left:46px;top:240px;width:132px;height:40px;line-height:36px;border:2px solid var(--teal);color:var(--teal);font-size:12px}

/* contact */
.contact-title{left:0;width:1200px;top:2283px;text-align:center;font-family:"Open Sans",sans-serif;font-weight:700;font-size:34px;color:var(--nav)}
.field{width:364px;height:50px;border:2px solid var(--line);border-radius:25px;padding:0 28px;line-height:46px;font-size:15px;color:#333;background:#fff}
.field.msg{width:744px;height:114px;border-radius:30px;line-height:40px}
.submit{left:474px;top:2633px;width:240px;height:54px;line-height:54px;background:var(--blue);color:#fff;font-size:17px}

/* footer */
.foot-wave{left:0;top:2720px}
.foot-mark{left:560px;top:2775px;width:80px;height:80px;border-radius:50%;background:var(--teal);border:4px solid #fff}
.social{left:482px;top:2878px;display:flex;gap:6px}
.social span{width:45px;height:45px;border:2px solid #fff;border-radius:50%;display:block}
.footnav{left:0;width:1200px;top:2948px;display:flex;justify-content:center;gap:44px}
.footnav a{font-family:"Open Sans",sans-serif;font-weight:600;font-size:16px;color:#fff;text-decoration:none}
.copy{left:0;width:1200px;top:2986px;text-align:center;font-size:14px;color:#fff}
</style>
</head>
<body>

<header>
  <div class="abs brand">
    <span class="brand-mark"></span>
    <div>
      <div class="brand-name">WHOLE HEART WELLBEING</div>
      <div class="brand-sub">PSYCHOLOGY &amp; COUNSELLING RELATIONSHIP CENTRE</div>
    </div>
  </div>
  <div class="abs contact-info ci-a">Text/Call:&nbsp; 0400 123 456<br>0400 654 321</div>
  <div class="abs contact-info ci-b">Tel.: (02) 9000 1234<br>Email:hello@wholeheartwellbeing.example</div>
</header>

<nav class="abs mainnav">
  <a class="on" href="#" style="margin-right:36px">HOW WE CAN HELP</a>
  <a href="#" style="margin-right:36px">RELATIONSHIP COUNSELLING</a>
  <a href="#" style="margin-right:30px">PARENTING</a>
  <a href="#" style="margin-right:25px">COURSES</a>
  <a href="#" style="margin-right:30px">OUR TEAM</a>
  <a href="#">CONTACT</a>
</nav>

<section>
  <div class="abs hero-photo" role="img" aria-label="Photo of a couple embracing on a sofa during a counselling session"></div>
  <div class="abs hero-panel">
    <h1>PSYCHOLOGY AND<br>COUNSELLING</h1>
    <span class="ghost-btn">LEARN MORE</span>
  </div>
  <div class="abs dots"><i></i><i></i><i class="on"></i><i></i><i></i></div>
  <svg class="abs wave" width="1200" height="130" viewBox="0 0 1200 130" aria-hidden="true">
    <path d="M0 130 L0 60 C200 120 420 110 600 60 C800 10 1000 10 1200 60 L1200 130 Z" fill="#fff"/>
    <path d="M0 60 C200 120 420 110 600 58 L600 68 C420 118 200 130 0 78 Z" fill="var(--teal)"/>
    <path d="M560 72 C760 5 1000 0 1200 45 L1200 105 C1000 30 780 25 560 80 Z" fill="var(--sky)"/>
  </svg>
</section>

<section>
  <div class="abs who-photo" role="img" aria-label="Photo of a counsellor talking with a client"></div>
  <h2 class="abs who-title">WHO WE HELP</h2>
  <p class="abs who-text">Whole Heart Wellbeing Psychology and Counselling Relationship Centre is a team of highly trained professionals provide the ultimate in wellbeing treatment for children, teenagers, adults, parents and couples. We have a strong reputation for providing a warm and personalised service using research based approaches.</p>
  <span class="abs pill who-btn">READ MORE</span>
</section>

<section class="abs expect" role="img" aria-label="Photo of a mother and child under a teal to blue overlay">
  <h2>WHAT TO EXPECT</h2>
  <p>Sometimes people don’t know what to expect from the counselling processes. You may wonder if your issues are too complicated, or not serious enough, or worry that the things you’ll discuss will be so distressing that you’ll carry the pain around with you, long after leaving the session.</p>
  <p>What people may not realise is that good therapy can be a joyful experience,<br>despite the need to discuss stressful, sad or shameful things.</p>
  <span class="pill">READ MORE</span>
</section>

<section>
  <div class="abs services" role="img" aria-label="Faded photo of a smiling family"></div>
  <div class="abs card" style="left:105px">
    <div class="card-icon"><span></span></div>
    <h3>Couples</h3>
    <p>Treatment for couples over 18 years old. We work with married couples, people in life partnerships and same sex couples and provide counselling services to improve the quality of relationships.</p>
    <span class="pill">VIEW SERVICES</span>
  </div>
  <div class="abs card" style="left:357px">
    <div class="card-icon"><span></span></div>
    <h3>Parenting</h3>
    <p>We work with parents to improve the quality of relationships between parent and child. We also work with new parents and parents who maybe suffering with post or peri natal depression.</p>
    <span class="pill">VIEW SERVICES</span>
  </div>
  <div class="abs card" style="left:611px">
    <div class="card-icon"><span></span></div>
    <h3>Adults</h3>
    <p>Treatment for individuals over 18 years old. We work with men and women and treat a wide range of mental health issues.</p>
    <span class="pill">VIEW SERVICES</span>
  </div>
  <div class="abs card" style="left:864px">
    <div class="card-icon"><span></span></div>
    <h3 style="margin-top:70px">Childrens &amp;<br>Teenagers</h3>
    <p>Treatment for individuals up to 18 year olds. We work with boys, girls, young adults and their parents and treat a wide range of mental health issues.</p>
    <span class="pill">VIEW SERVICES</span>
  </div>
</section>

<section>
  <h2 class="abs contact-title">CONTACT US</h2>
  <div class="abs field" style="left:222px;top:2358px">Enter Name</div>
  <div class="abs field" style="left:602px;top:2358px">Enter Email</div>
  <div class="abs field" style="left:222px;top:2423px">Phone</div>
  <div class="abs field" style="left:602px;top:2423px">Address</div>
  <div class="abs field msg" style="left:222px;top:2488px">Message</div>
  <span class="abs pill submit">SUBMIT MESSAGE</span>
</section>

<footer>
  <svg class="abs foot-wave" width="1200" height="350" viewBox="0 0 1200 350" aria-hidden="true">
    <path d="M0 20 C150 110 380 110 600 80 C800 50 1000 -10 1200 20 L1200 350 L0 350 Z" fill="var(--sky)"/>
    <path d="M0 60 C180 140 400 130 600 95 C800 60 1000 20 1200 45 L1200 350 L0 350 Z" fill="#fff"/>
    <path d="M0 70 C180 150 400 140 600 105 C800 70 1000 30 1200 55 L1200 350 L0 350 Z" fill="var(--navy)"/>
  </svg>
  <span class="abs foot-mark"></span>
  <div class="abs social" aria-label="Social media links"><span></span><span></span><span></span><span></span><span></span></div>
  <nav class="abs footnav">
    <a href="#">HOW WE CAN HELP</a><a href="#">RELATIONSHIP COUNSELLING</a><a href="#">PARENTING</a><a href="#">COURSES</a><a href="#">OUR TEAM</a><a href="#">CONTACT</a>
  </nav>
  <p class="abs copy">© 2019 Company Name&nbsp; All right reserved</p>
</footer>

</body>
</html>
```